We are a new company with 2 divisions a medical research and medical product sales. We need a company logo and Business Cards. The design files need to be provided to us in Adobe Photoshop CS 5.1.

Target Market(s)

Medical Community

Industry/Entity Type

Medical

Contact Information for Business Card

Company Name - Larkmoor Biomedical LLC
Company Address 4217 NE 14th Ave Suite 7, Gainesville Fl 32609

Requirements
Must have
• The design files need to be provided to us in Adobe Photoshop CS 5.1.

```html
<!DOCTYPE html>
<html lang="en">
<head>
<meta charset="utf-8">
<title>Larkmoor Biomedical LLC – Business Card</title>
<link href="https://fonts.googleapis.com/css2?family=Arimo:wght@400;700&display=swap" rel="stylesheet">
<style>
  :root {
    --paper: #ffffff;
    --ink: #111111;
    --teal: #2a7f70;
    --teal-soft: #9dbdb7;
  }
  html, body {
    margin: 0;
    padding: 0;
    overflow: hidden;
    background: var(--paper);
  }
  .card {
    position: relative;
    width: 1200px;
    height: 686px;
    background: var(--paper);
    font-family: "Arimo", "Helvetica Neue", Arial, sans-serif;
    overflow: hidden;
  }
  .brand-mark {
    position: absolute;
    left: 46px;
    top: 168px;
    width: 160px;
    display: flex;
    flex-direction: column;
    align-items: center;
    gap: 14px;
  }
  .brand-mark svg {
    display: block;
  }
  .brand-name {
    margin: 0;
    font-size: 26px;
    font-weight: 400;
    color: var(--teal);
    line-height: 1;
  }
  .company {
    position: absolute;
    left: 435px;
    top: 193px;
    margin: 0;
    font-size: 34px;
    font-weight: 700;
    line-height: 1;
    color: var(--ink);
    letter-spacing: 0.2px;
  }
  .person {
    position: absolute;
    left: 435px;
    top: 288px;
    margin: 0;
    font-size: 35px;
    font-weight: 400;
    line-height: 1;
    color: var(--teal);
  }
  .address {
    position: absolute;
    left: 435px;
    top: 472px;
    margin: 0;
    font-style: normal;
    font-size: 35px;
    line-height: 46px;
    color: var(--teal-soft);
    letter-spacing: 0.3px;
  }
</style>
</head>
<body>
  <main class="card">
    <div class="brand-mark">
      <svg width="120" height="120" viewBox="0 0 120 120" aria-hidden="true">
        <circle cx="60" cy="60" r="58" fill="var(--teal)"/>
      </svg>
      <p class="brand-name">Larkmoor</p>
    </div>

    <h1 class="company">Larkmoor Biomedical LLC</h1>
    <p class="person">Daniel Reyes</p>

    <address class="address">
      4217 NE 14th Ave, Suite 7<br>
      Gainesville, FL 32609
    </address>
  </main>
</body>
</html>
```